MAVO VERTICAL & HORIZONTAL FOLDING STICKERS FOR PACKAGING

We are a California Dispensary that will be launching our marijuana brands. We would like to use the MAVO logo developed (attached) for one of our flower brands. We love the look and feel and believe it will provide great branding for us.

This product will be in black and clear bags for display at stores.

For the Bags, we will need vertical and horizontal packaging for our stickers. IMPORTANT TO NOTE, these stickers will be folding the stickers AROUND THE BAGS.

Additionally, there are restrictions about what needs to be on the package; a separate document is included with that information along with some examples.

For the VERTICAL STICKERS, we will be folding the strip to cover part of the front of the bag and part of the back of the bag. The front part should represent 70% of the label, and the back part (folded over) should be 30%. Please keep the warnings on the back.

For the HORIZONTAL, the fold will be broken out as 75% to 80% on the front of the bag, and 20 to 25% on the back of the bag.
For both VERTICAL AND HORIZONTAL, please keep the warnings on the back. Note, that we would like the strain name (e.g.: Amber Drift) to be very visible on the front of both of these.

The three sticker colors are glossy white, silver, and gold. If you choose to focus on the white sticker, please be sure to incorporate background color as you see fit to ensure the logo and packaging will pop on the shelves.

Sticker sizes are below for use in development of this packaging:
Roll Label: 5" x 2" High Gloss White Polypropylene (BOPP) (R31).
SQUARE CORNERS - 1300 labels per roll - 0.0156" corner radius - 0.125"gap (top / bottom), 0.0625"margin (left / right) - 3" core, 6" outside - minimum quantity 1
__
One item we like from the Ferrow Cannabis label example is the approach to the strain (hybrid, sativa, Indica). We will also have a strain name (eg: Amber Drift). I've enclosed picture examples but would be happy to provide more information.

```html
<!DOCTYPE html>
<html lang="en">
<head>
<meta charset="utf-8">
<title>MAVO Amber Drift – Folding Stickers</title>
<link href="https://fonts.googleapis.com/css2?family=Nunito:wght@400;800;900&family=Roboto+Condensed:wght@400;700&display=swap" rel="stylesheet">
<style>
  :root{
    --page:#ffffff;
    --label-top:#03252e;
    --label-mid:#1c7a34;
    --label-bottom:#48b835;
    --crack:#050a07;
    --brand-green:#8dc63f;
    --strain-green:#5fd13a;
    --strain-white:#f1f1f1;
    --text:#ffffff;
    --caution:#f7c21a;
    --caution-edge:#2a2a00;
  }
  *{margin:0;padding:0;box-sizing:border-box}
  html,body{width:1200px;height:879px;overflow:hidden;background:var(--page)}
  .canvas{position:relative;width:1200px;height:879px}
  .label{position:absolute;overflow:hidden;color:var(--text);
    background:linear-gradient(180deg,var(--label-top) 0%,#0f4a31 35%,var(--label-mid) 65%,var(--label-bottom) 100%)}
  .label--vertical{left:53px;top:74px;width:292px;height:731px}
  .label--horizontal{left:416px;top:293px;width:731px;height:292px}

  .gov-warning{font-family:"Roboto Condensed",sans-serif;font-size:9.4px;line-height:11.5px;
    text-transform:uppercase;text-align:justify;text-align-last:left}
  .gov-warning b{font-weight:700;letter-spacing:.6px}

  .p65{display:flex;align-items:center;gap:6px;font-family:"Nunito",sans-serif;font-size:10.4px;line-height:14px}
  .p65 b{font-weight:800}
  .p65__text{text-align:center}
  .caution-icon{width:42px;height:37px;flex:none}

  .blurb{font-family:"Nunito",sans-serif;font-size:10.3px;line-height:13.6px;text-align:center}

  .crack-art{position:absolute;border-radius:48% 52% 45% 55%/50% 46% 54% 50%;
    background:radial-gradient(ellipse at center,var(--crack) 0%,var(--crack) 55%,rgba(5,10,7,.55) 72%,rgba(5,10,7,0) 100%)}

  .brand{position:absolute;text-align:center;font-family:"Nunito",sans-serif}
  .brand__name{display:block;font-weight:900;font-size:34px;line-height:34px;letter-spacing:2px;color:var(--brand-green)}
  .brand__strain{display:block;font-weight:900;font-size:28px;line-height:29px;margin-top:14px;color:var(--strain-green)}
  .brand__strain span{display:block;color:var(--strain-white)}

  .net-wt{position:absolute;font-family:"Nunito",sans-serif;font-size:11px;line-height:13px;text-align:center}

  .state-badge{position:absolute;width:48px;height:52px}
</style>
</head>
<body>
<div class="canvas">

  <!-- Vertical folding sticker -->
  <section class="label label--vertical" aria-label="Vertical folding sticker">
    <p class="gov-warning" style="position:absolute;left:19px;top:30px;width:255px">
      <b>Government Warning</b>: This product contains cannabis, a schedule I controlled substance. Keep out of reach of children and animals. Cannabis products may only be possessed or consumed by persons 21 years of age or older unless the person is a qualified patient. The intoxicating effects of cannabis products may be delayed up to two hours. Cannabis use while pregnant or breastfeeding may be harmful. Consumption of cannabis products impairs your ability to drive and operate machinery. Please use extreme caution.
    </p>
    <div class="p65" style="position:absolute;left:19px;top:160px;width:262px">
      <svg class="caution-icon" viewBox="0 0 42 37" aria-hidden="true"><path d="M21 2 L40 34 H2 Z" fill="var(--caution)" stroke="var(--caution-edge)" stroke-width="2.5" stroke-linejoin="round"/><rect x="19" y="12" width="4" height="13" rx="1.5" fill="#111"/><circle cx="21" cy="29" r="2.2" fill="#111"/></svg>
      <p class="p65__text"><b>WARNING:</b> Cancer and reproductive harm.<br>www.safetynotice-ca.org</p>
    </div>
    <p class="blurb" style="position:absolute;left:22px;top:214px;width:248px">
      Lorem ipsum dolor sit amet, consectetur adipiscing elit. Mauris eu eros tellus. Aenean ac lacus ut ante dictum blandit. In commodo tempus mi, quis aliquet est hendrerit vel. Quisque at metus nibh. Phasellus vehicula sem tortor, sit amet fermentum dolor pretium et. Proin eget elit sed ligula venenatis maximus ac id nulla. Vivamus non nisi lacus. Aenean nisi diam, facilisis eget sollicitudin ut, ultricies hendrerit leo. Lorem ipsum dolor sit amet, consectetur adipiscing elit. Proin a volutpat nibh. Class aptent taciti sociosqu ad litora torquent per conubia nostra, per inceptos himenaeos.
    </p>
    <div class="crack-art" role="img" aria-label="Illustration of a cracked hole breaking through the green surface" style="left:-2px;top:430px;width:296px;height:300px"></div>
    <div class="brand" style="left:46px;top:530px;width:200px">
      <span class="brand__name">MAVO</span>
      <span class="brand__strain">AMBER<span>DRIFT</span></span>
    </div>
    <p class="net-wt" style="left:26px;top:681px">NET WT<br>1/4oz (7g)</p>
    <svg class="state-badge" style="left:134px;top:660px" viewBox="0 0 48 52" role="img" aria-label="State compliance badge"><path d="M24 3 L45 40 H3 Z" fill="#0c5a2c" stroke="#fff" stroke-width="3" stroke-linejoin="round"/><rect x="8" y="41" width="32" height="10" rx="4" fill="#0c5a2c" stroke="#fff" stroke-width="2"/></svg>
  </section>

  <!-- Horizontal folding sticker -->
  <section class="label label--horizontal" aria-label="Horizontal folding sticker">
    <div class="crack-art" role="img" aria-label="Illustration of a cracked hole breaking through the green surface" style="left:34px;top:8px;width:300px;height:284px"></div>
    <div class="brand" style="left:79px;top:85px;width:200px">
      <span class="brand__name">MAVO</span>
      <span class="brand__strain">AMBER<span>DRIFT</span></span>
    </div>
    <p class="net-wt" style="left:71px;top:255px">NET WT<br>1/4oz (7g)</p>
    <svg class="state-badge" style="left:174px;top:232px" viewBox="0 0 48 52" role="img" aria-label="State compliance badge"><path d="M24 3 L45 40 H3 Z" fill="#0c5a2c" stroke="#fff" stroke-width="3" stroke-linejoin="round"/><rect x="8" y="41" width="32" height="10" rx="4" fill="#0c5a2c" stroke="#fff" stroke-width="2"/></svg>
    <p class="blurb" style="position:absolute;left:338px;top:25px;width:188px">
      Lorem ipsum dolor sit amet, consectetur adipiscing elit. Mauris eu eros tellus. Aenean ac lacus ut ante dictum blandit. In commodo tempus mi, quis aliquet est hendrerit vel. Quisque at metus nibh. Phasellus vehicula sem tortor, sit amet fermentum dolor pretium et. Proin eget elit sed ligula venenatis maximus ac id nulla. Vivamus non nisi lacus. Aenean nisi diam, facilisis eget sollicitudin ut, ultricies hendrerit leo. Lorem ipsum dolor sit amet, consectetur adipiscing elit. Proin a volutpat nibh. Class aptent taciti sociosqu ad litora torquent per conubia nostra, per inceptos himenaeos.
    </p>
    <div class="p65" style="position:absolute;left:432px;top:131px;width:260px;transform:rotate(-90deg)">
      <svg class="caution-icon" viewBox="0 0 42 37" aria-hidden="true" style="transform:rotate(90deg)"><path d="M21 2 L40 34 H2 Z" fill="var(--caution)" stroke="var(--caution-edge)" stroke-width="2.5" stroke-linejoin="round"/><rect x="19" y="12" width="4" height="13" rx="1.5" fill="#111"/><circle cx="21" cy="29" r="2.2" fill="#111"/></svg>
      <p class="p65__text"><b>WARNING:</b> Cancer and reproductive harm.<br>www.safetynotice-ca.org</p>
    </div>
    <p class="gov-warning" style="position:absolute;left:521px;top:81px;width:254px;transform:rotate(-90deg)">
      <b>Government Warning</b>: This product contains cannabis, a schedule I controlled substance. Keep out of reach of children and animals. Cannabis products may only be possessed or consumed by persons 21 years of age or older unless the person is a qualified patient. The intoxicating effects of cannabis products may be delayed up to two hours. Cannabis use while pregnant or breastfeeding may be harmful. Consumption of cannabis products impairs your ability to drive and operate machinery. Please use extreme caution.
    </p>
  </section>

</div>
</body>
</html>
```